Real Estate Investment Company Needs A Business Card Designed

I need a business card designed for my use. We are a real estate investment company based in Omaha, Nebraska that specializes in buying, rehabbing and selling single family and multifamily properties. Would love designs that incorporate our logo and colors

Industry/Entity Type

Business

Contact Information for Business Card

Mitchell Parkhurst | President & CEO
4873 North 52nd Avenue, Ste 700
Omaha, NE 68142
(402) 786-4259
mitchell@kestrelgateproperties.example
www.KestrelgateProperties.example

Font styles to use
Serif

Colors
0255a3
3276b5

Requirements
Must have
• Our logo

```html
<!DOCTYPE html>
<html lang="en">
<head>
<meta charset="utf-8">
<title>Kestrelgate Properties – Business Card</title>
<link rel="stylesheet" href="https://fonts.googleapis.com/css2?family=Questrial&display=swap">
<style>
  :root {
    --backdrop: #e4e2de;
    --card-black: #050607;
    --black-sheen: #1c1e21;
    --blue: #0255a3;
    --blue-light: #3276b5;
    --blue-bright: #2a8fd8;
    --blue-deep: #0a2f86;
    --grey: #c9cbce;
    --grey-light: #e3e4e6;
    --white: #ffffff;
  }
  * { margin: 0; padding: 0; box-sizing: border-box; }
  html, body {
    width: 1200px; height: 1200px; overflow: hidden;
    background: var(--backdrop);
    font-family: "Questrial", sans-serif;
  }
  .sheet {
    width: 1200px; height: 1200px;
    display: flex; flex-direction: column; align-items: center; justify-content: center;
    gap: 60px;
  }
  .card {
    position: relative; width: 840px; height: 480px; overflow: hidden;
    background: linear-gradient(125deg, var(--black-sheen) 0%, var(--card-black) 45%, var(--card-black) 100%);
    box-shadow: 0 10px 30px rgba(0,0,0,.25);
  }
  .card-art { position: absolute; inset: 0; }

  /* brand mark stand-in */
  .brand { position: absolute; display: flex; align-items: center; gap: 16px; color: var(--blue-light); }
  .brand-dot { border-radius: 50%; background: var(--blue-light); flex: none; }
  .brand-name { text-transform: uppercase; line-height: 1.05; letter-spacing: .04em; }
  .card-front .brand { left: 50%; top: 50%; transform: translate(-50%, -50%); }
  .card-front .brand-dot { width: 70px; height: 70px; }
  .card-front .brand-name { font-size: 46px; }
  .card-back .brand { left: 110px; top: 130px; }
  .card-back .brand-dot { width: 44px; height: 44px; }
  .card-back .brand-name { font-size: 30px; }

  /* name plate */
  .name-plate { position: absolute; left: 500px; top: 112px; width: 320px; color: var(--white); }
  .person-name { font-size: 30px; text-transform: uppercase; letter-spacing: .02em; color: var(--white); text-shadow: 0 1px 0 rgba(0,0,0,.15); }
  .person-title { font-size: 22px; text-transform: uppercase; color: var(--blue-light); margin-top: 2px; }

  .tagline {
    position: absolute; left: 32px; top: 302px; width: 560px;
    font-size: 18px; font-weight: 700; color: var(--blue); line-height: 1.2;
  }

  .contact { position: absolute; color: var(--white); font-size: 17px; line-height: 1.35; list-style: none; }
  .contact li { display: flex; align-items: flex-start; gap: 12px; margin-bottom: 6px; }
  .contact svg { width: 18px; height: 18px; flex: none; margin-top: 2px; fill: var(--white); }
  .contact-left { left: 60px; top: 386px; }
  .contact-right { left: 430px; top: 386px; }
</style>
</head>
<body>
<main class="sheet">

  <section class="card card-front" aria-label="Card front">
    <div class="brand">
      <span class="brand-dot"></span>
      <span class="brand-name">Kestrelgate<br>Properties</span>
    </div>
  </section>

  <section class="card card-back" aria-label="Card back">
    <svg class="card-art" viewBox="0 0 840 480" aria-hidden="true">
      <defs>
        <linearGradient id="blueSide" x1="0" y1="0" x2="0" y2="1">
          <stop offset="0" stop-color="#2a8fd8"/>
          <stop offset="1" stop-color="#0255a3"/>
        </linearGradient>
        <linearGradient id="blueBase" x1="0" y1="0" x2="1" y2="0">
          <stop offset="0" stop-color="#0a2f86"/>
          <stop offset="1" stop-color="#0255a3"/>
        </linearGradient>
        <linearGradient id="greyFade" x1="0" y1="0" x2="1" y2="0">
          <stop offset="0" stop-color="#b9bbbf"/>
          <stop offset="1" stop-color="#e3e4e6"/>
        </linearGradient>
      </defs>
      <!-- right blue column -->
      <path class="blue-column" d="M610 70 Q610 40 640 40 H840 V480 H610 Z" fill="url(#blueSide)"/>
      <!-- grey tagline band -->
      <path class="grey-band" d="M0 292 H576 Q600 292 600 316 V372 H0 Z" fill="url(#greyFade)"/>
      <!-- blue base -->
      <rect class="blue-base" x="0" y="364" width="840" height="116" fill="url(#blueBase)"/>
      <!-- name plate -->
      <path class="grey-plate" d="M512 96 H840 V210 H512 Q486 210 486 184 V122 Q486 96 512 96 Z" fill="url(#greyFade)"/>
    </svg>

    <div class="brand">
      <span class="brand-dot"></span>
      <span class="brand-name">Kestrelgate<br>Properties</span>
    </div>

    <div class="name-plate">
      <h1 class="person-name">Mitchell Parkhurst</h1>
      <p class="person-title">President &amp; CEO</p>
    </div>

    <p class="tagline">Specializes in Buying, Rehabbing, Selling single family and multifamily properties.</p>

    <ul class="contact contact-left">
      <li>
        <svg viewBox="0 0 24 24"><path d="M6.6 10.8a15 15 0 0 0 6.6 6.6l2.2-2.2a1 1 0 0 1 1-.25 11.4 11.4 0 0 0 3.6.57 1 1 0 0 1 1 1V20a1 1 0 0 1-1 1A17 17 0 0 1 3 4a1 1 0 0 1 1-1h3.5a1 1 0 0 1 1 1c0 1.25.2 2.45.57 3.57a1 1 0 0 1-.25 1z"/></svg>
        <span>(402) 786-4259</span>
      </li>
      <li>
        <svg viewBox="0 0 24 24"><path d="M12 2a7 7 0 0 0-7 7c0 5.25 7 13 7 13s7-7.75 7-13a7 7 0 0 0-7-7zm0 9.5A2.5 2.5 0 1 1 12 6.5a2.5 2.5 0 0 1 0 5z"/></svg>
        <span>4873 North 52nd Avenue, Ste 700<br>Omaha, NE 68142</span>
      </li>
    </ul>

    <ul class="contact contact-right">
      <li>
        <svg viewBox="0 0 24 24"><path d="M12 2a10 10 0 1 0 0 20 10 10 0 0 0 0-20zm6.9 6h-2.9a15.6 15.6 0 0 0-1.4-3.6A8 8 0 0 1 18.9 8zM12 4c.8 1.2 1.5 2.5 1.9 4h-3.8c.4-1.5 1.1-2.8 1.9-4zM4.3 14a8 8 0 0 1 0-4h3.4a16 16 0 0 0 0 4zm.8 2h2.9c.3 1.3.8 2.5 1.4 3.6A8 8 0 0 1 5.1 16zM8 8H5.1a8 8 0 0 1 4.3-3.6C8.8 5.5 8.3 6.7 8 8zm4 12c-.8-1.2-1.5-2.5-1.9-4h3.8c-.4 1.5-1.1 2.8-1.9 4zm2.3-6H9.7a14.7 14.7 0 0 1 0-4h4.6a14.7 14.7 0 0 1 0 4zm.3 5.6c.6-1.1 1.1-2.3 1.4-3.6h2.9a8 8 0 0 1-4.3 3.6zM16.3 14a16 16 0 0 0 0-4h3.4a8 8 0 0 1 0 4z"/></svg>
        <span>www.KestrelgateProperties.example</span>
      </li>
      <li>
        <svg viewBox="0 0 24 24"><path d="M3 5h18a1 1 0 0 1 1 1v12a1 1 0 0 1-1 1H3a1 1 0 0 1-1-1V6a1 1 0 0 1 1-1zm9 7.5L4 7.2V8l8 5.3L20 8v-.8z"/></svg>
        <span>mitchell@kestrelgateproperties.example</span>
      </li>
    </ul>
  </section>

</main>
</body>
</html>
```